Webdesign für Automotive Engineering Webpage
Automotive Engineering - Main focus is Software Development & Embedded systems for the Automotive industry.
Like as HMI, ADAS, ECU
See Logo (PDF), example --> https://www.brantlex.com/de/de (competetor)

```html
<!DOCTYPE html>
<html lang="de">
<head>
<meta charset="utf-8">
<title>HALDRIS – Die Nr. 1 in Engineering</title>
<link href="https://fonts.googleapis.com/css2?family=Bebas+Neue&family=Open+Sans:wght@300;400;600;700&display=swap" rel="stylesheet">
<style>
:root{
  --red:#e30613;
  --navy:#141a2e;
  --navy-deep:#10152a;
  --box:rgba(36,42,62,.72);
  --white:#ffffff;
  --ink:#2b3040;
  --muted:#8a90a0;
  --hero-muted:#9ba1b3;
  --steel:#c9d4e2;
  --rule:#d9dce3;
  --pale:#d6dfeb;
}
*{box-sizing:border-box;margin:0;padding:0}
html,body{width:1200px;height:2871px;overflow:hidden}
body{position:relative;background:var(--white);font-family:"Open Sans",Arial,sans-serif;color:var(--ink)}
a{text-decoration:none}
.display{font-family:"Bebas Neue","Oswald",sans-serif;font-weight:400;letter-spacing:.2px}
.btn{position:absolute;display:flex;align-items:center;justify-content:center;background:var(--red);color:var(--white);border-radius:14px;font-size:11px;font-weight:700;letter-spacing:.3px;text-transform:uppercase}

/* hero */
.hero{position:absolute;left:0;top:0;width:1200px;height:833px;background:linear-gradient(180deg,#1a2035 0%,var(--navy) 60%,#121729 100%)}
.hero-side{position:absolute;left:0;top:0;width:339px;height:833px;background:linear-gradient(160deg,#3a4154 0%,#2a3044 45%,#1e2438 100%)}
.hero-car{position:absolute;left:117px;top:236px;width:434px;height:158px;border-radius:50% 50% 30% 30%/70% 70% 30% 30%;background:radial-gradient(ellipse at 50% 45%,#5a5e66 0%,#3a3d45 45%,rgba(30,32,40,0) 75%)}
.brand{position:absolute;color:var(--white);font-weight:700;font-size:15px;letter-spacing:1.5px;display:flex;align-items:center;gap:6px}
.brand .dot{width:7px;height:7px;border-radius:50%;background:var(--red)}
.nav{position:absolute;top:30px;font-size:11px;font-weight:700;color:var(--white);letter-spacing:.4px}
.menu-btn{position:absolute;left:1133px;top:0;width:67px;height:67px;background:var(--red)}
.follow{position:absolute;left:44px;top:148px;color:var(--white);font-size:8px;font-weight:700;letter-spacing:.5px;transform:rotate(90deg);transform-origin:left top;white-space:nowrap}
.follow-line{position:absolute;left:38px;top:200px;width:1px;height:134px;background:rgba(255,255,255,.45)}
.social{position:absolute;left:33px;width:12px;height:12px;border-radius:50%;background:#d7dae2}
.hero-title{position:absolute;left:644px;top:220px;font-size:53px;line-height:1;color:#cfd3de;white-space:nowrap}
.hero-title em{font-style:normal;color:var(--red)}
.hero-sub{position:absolute;left:644px;top:284px;font-size:13.5px;line-height:19px;color:var(--hero-muted)}
.features{position:absolute;left:134px;top:548px;width:932px;height:236px;background:var(--box);border-radius:4px}
.feature{position:absolute;top:58px;width:300px;text-align:center}
.feature svg{display:block;margin:0 auto}
.feature h3{margin-top:18px;font-size:21px;color:#e6e8ee;line-height:1}
.feature p{margin-top:14px;font-size:13px;line-height:19px;color:var(--hero-muted)}

/* services */
.service{position:absolute;width:260px;text-align:center}
.service svg{display:block;margin:0 auto}
.service h3{font-size:20px;line-height:1;color:var(--ink);margin-top:18px}
.service p{font-size:13px;line-height:20px;color:var(--muted);margin-top:14px}
.pod-backdrop{position:absolute;left:827px;top:941px}
.pod{position:absolute;left:744px;top:1030px;width:379px;height:312px;border-radius:48% 52% 40% 45%/55% 50% 50% 45%;background:radial-gradient(ellipse at 60% 45%,#ffffff 0%,#e8edf3 45%,#a9b4c2 80%,#7d8796 100%)}
.divider{position:absolute;left:0;top:1577px;width:827px;height:1px;background:var(--rule)}

/* blog */
.blog-heading{position:absolute;left:134px;top:1994px;transform:rotate(-90deg);transform-origin:left top;white-space:nowrap}
.blog-heading .light{display:block;font-size:31px;font-weight:300;color:var(--ink);line-height:34px}
.blog-heading .bold{display:block;font-size:31px;font-weight:700;color:var(--ink);line-height:34px;letter-spacing:.5px}
.arrow-btn{position:absolute;top:1665px;width:46px;height:46px;background:var(--steel)}
.blog-track{position:absolute;left:228px;top:1716px;width:839px;height:520px;overflow:hidden}
.post{position:absolute;top:0;width:300px;height:516px;border-bottom:2px solid #2f3446}
.post-media{width:300px;height:249px}
.post h3{margin-top:36px;text-align:center;font-size:20px;line-height:1;color:var(--ink);white-space:nowrap}
.post p{margin:14px auto 0;width:240px;text-align:center;font-size:13px;line-height:18.5px;color:var(--muted)}
.post .more{display:block;margin-top:40px;text-align:center;font-size:11px;font-weight:700;color:var(--red);letter-spacing:.3px}

/* newsletter + footer */
.newsletter{position:absolute;left:0;top:2387px;width:1200px;height:484px;background:radial-gradient(ellipse at 55% 35%,#242a40 0%,#181d31 50%,var(--navy-deep) 100%)}
.nl-icon{position:absolute;left:583px;top:2466px}
.nl-kicker{position:absolute;left:0;width:1200px;top:2513px;text-align:center;font-size:20px;font-weight:300;color:#c8ccd8}
.nl-title{position:absolute;left:0;width:1200px;top:2540px;text-align:center;font-size:20px;font-weight:700;color:#e6e8ee;letter-spacing:.3px}
.nl-form{position:absolute;left:455px;top:2594px;width:290px;height:24px;border:1px solid var(--red);border-radius:12px;overflow:hidden;display:flex}
.nl-input{flex:0 0 189px;padding-left:10px;display:flex;align-items:center;font-size:11px;color:#c8ccd8}
.nl-submit{flex:1;background:var(--red);color:var(--white);font-size:11px;font-weight:700;display:flex;align-items:center;justify-content:center}
.copyright{position:absolute;left:128px;top:2822px;font-size:11px;color:#c8ccd8}
.footer-link{position:absolute;top:2798px;font-size:11px;font-weight:700;color:var(--white);letter-spacing:.3px}
</style>
</head>
<body>

<section class="hero">
  <div class="hero-side" role="img" aria-label="Dunkles Foto eines Sportwagens im Anschnitt"></div>
  <div class="hero-car" role="img" aria-label="Freigestellter grauer Supersportwagen"></div>

  <div class="brand" style="left:33px;top:30px"><span>HALDRIS</span><span class="dot"></span></div>

  <span class="nav" style="left:792px">HOME</span>
  <span class="nav" style="left:870px">KOMPETENZEN</span>
  <span class="nav" style="left:999px">KARRIERE</span>
  <div class="menu-btn">
    <svg width="67" height="67" viewBox="0 0 67 67"><g stroke="#fff" stroke-width="1.6"><line x1="22" y1="27" x2="45" y2="27"/><line x1="27" y1="33" x2="45" y2="33"/><line x1="32" y1="39" x2="45" y2="39"/></g></svg>
  </div>

  <span class="follow">FOLLOW US</span>
  <div class="follow-line"></div>
  <span class="social" style="top:369px"></span>
  <span class="social" style="top:403px"></span>
  <span class="social" style="top:436px"></span>
  <span class="social" style="top:470px"></span>

  <h1 class="hero-title display">DIE <em>NR. 1</em> IN ENGINEERING</h1>
  <p class="hero-sub">Beste internationale fahrzeugtechnische<br>Dienstleistungen für das Engineering</p>
  <a class="btn" style="left:644px;top:354px;width:129px;height:25px">LEARN MORE</a>

  <div class="features">
    <div class="feature" style="left:0">
      <svg width="40" height="40" viewBox="0 0 40 40" fill="none" stroke="#e30613" stroke-width="1.6"><circle cx="20" cy="20" r="6"/><path d="M17 3h6l1 5 4 2 4-3 4 4-3 4 2 4 5 1v6l-5 1-2 4 3 4-4 4-4-3-4 2-1 5h-6l-1-5-4-2-4 3-4-4 3-4-2-4-5-1v-6l5-1 2-4-3-4 4-4 4 3 4-2z"/></svg>
      <h3 class="display">FÜR KUNDEN</h3>
      <p>Kundenspezifische<br>Technische Lösungen</p>
    </div>
    <div class="feature" style="left:316px">
      <svg width="40" height="40" viewBox="0 0 40 40" fill="none" stroke="#e30613" stroke-width="1.6"><rect x="4" y="11" width="32" height="24" rx="2"/><path d="M14 11V6h12v5M13 11v24M27 11v24"/></svg>
      <h3 class="display">ERREICHEN SIE MIT UNS DIE TOP-KARRIERE</h3>
      <p>Ingenieure Berater<br>Gesucht</p>
    </div>
    <div class="feature" style="left:632px">
      <svg width="40" height="40" viewBox="0 0 40 40" fill="none" stroke="#e30613" stroke-width="1.6"><circle cx="15" cy="11" r="6"/><path d="M3 35c0-7 5-12 12-12s12 5 12 12zM24 5a6 6 0 0 1 0 12M29 23c5 1 8 6 8 12h-4"/></svg>
      <h3 class="display">FÜR FREELANCER</h3>
      <p>Ein starker Partner für Ihr<br>Unternehmen</p>
    </div>
  </div>
</section>

<div class="service" style="left:153px;top:971px">
  <svg width="38" height="38" viewBox="0 0 40 40" fill="none" stroke="#e30613" stroke-width="1.6"><rect x="4" y="11" width="32" height="24" rx="2"/><path d="M14 11V6h12v5M13 11v24M27 11v24"/></svg>
  <h3 class="display">KARRIERE IM VERTRIEB</h3>
  <p>Es ist deine Zeit</p>
</div>
<a class="btn" style="left:204px;top:1124px;width:158px;height:24px">JETZT ÜBERZEUGEN</a>

<div class="service" style="left:438px;top:967px">
  <svg width="38" height="42" viewBox="0 0 38 42" fill="none" stroke="#e30613" stroke-width="1.6"><circle cx="19" cy="14" r="11"/><path d="M12 23l-2 17 9-6 9 6-2-17"/></svg>
  <h3 class="display">YOUR NAVIGATION TO EXPERTS</h3>
  <p>120.000 Experten Warten Auf Sie</p>
</div>
<a class="btn" style="left:490px;top:1124px;width:158px;height:24px">JETZT TESTEN</a>

<div class="service" style="left:153px;top:1227px">
  <svg width="52" height="38" viewBox="0 0 52 38" fill="none" stroke="#e30613" stroke-width="1.6"><circle cx="26" cy="10" r="7"/><path d="M13 36c0-8 6-14 13-14s13 6 13 14M11 6a5 5 0 0 0 0 10M41 6a5 5 0 0 1 0 10M2 34c0-6 4-11 9-11M50 34c0-6-4-11-9-11"/></svg>
  <h3 class="display">GESCHÄFTSFELD DIRECT</h3>
  <p>Wir Bieten Peronalberatung und<br>Platzierung</p>
</div>
<a class="btn" style="left:204px;top:1399px;width:158px;height:25px">JETZT INFORMIEREN</a>

<div class="service" style="left:438px;top:1227px">
  <svg width="34" height="40" viewBox="0 0 34 40" fill="none" stroke="#e30613" stroke-width="1.6"><path d="M17 2l14 5v12c0 9-6 15-14 19C9 34 3 28 3 19V7z"/></svg>
  <h3 class="display">VERMEIDEN SIE MIT UNS RISIKEN</h3>
  <p>Rechtskon Formität Bei Werk- Und<br>Dienstverträgen</p>
</div>
<a class="btn" style="left:490px;top:1399px;width:158px;height:25px">JETZT ÜBERZEUGEN</a>

<svg class="pod-backdrop" width="193" height="483" viewBox="0 0 193 483"><path d="M193 0V290A193 193 0 0 1 0 483V193A193 193 0 0 1 193 0Z" fill="#d6dfeb"/></svg>
<div class="pod" role="img" aria-label="Weißes futuristisches Einrad-Fahrzeug mit Glaskuppel"></div>

<div class="divider"></div>

<h2 class="blog-heading"><span class="light">UNSER BLOG</span><span class="bold">LESEN SIE TECHNIK</span></h2>
<div class="arrow-btn" style="left:228px"><svg width="46" height="46" viewBox="0 0 46 46"><path d="M26 15l-8 8 8 8" fill="none" stroke="#fff" stroke-width="2.4"/></svg></div>
<div class="arrow-btn" style="left:279px"><svg width="46" height="46" viewBox="0 0 46 46"><path d="M20 15l8 8-8 8" fill="none" stroke="#fff" stroke-width="2.4"/></svg></div>

<div class="blog-track">
  <article class="post" style="left:0">
    <div class="post-media"></div>
    <h3 class="display">IRRWITZ IM WECKER</h3>
    <p>Lorem ipsum dolor sit amet, consectetur adipiscing elit. Sodales adipiscing eget iaculis amet morbi. Egestas ipsum massa dolor gravida. A mattis viverra et malesuada mollis rhoncus tincidunt. Ante suspendisse sed risus est vitae convallis felis.</p>
    <a class="more">WEITERLESEN ›</a>
  </article>
  <article class="post" style="left:335px">
    <div class="post-media" role="img" aria-label="Beleuchteter Drehzahlmesser im dunklen Cockpit" style="background:radial-gradient(ellipse at 50% 80%,#3a0a0c 0%,#0a0a12 55%,#05060a 100%)"></div>
    <h3 class="display">LICHT AM ENDE DES TUNNELS</h3>
    <p>Lorem ipsum dolor sit amet, consectetur adipiscing elit. Sodales adipiscing eget iaculis amet morbi. Egestas ipsum massa dolor gravida. A mattis viverra et malesuada mollis rhoncus tincidunt. Ante suspendisse sed risus est vitae convallis felis.</p>
    <a class="more">WEITERLESEN ›</a>
  </article>
  <article class="post" style="left:668px">
    <div class="post-media" role="img" aria-label="Motorraum mit Leitungen in blauem Licht" style="background:linear-gradient(150deg,#1d2c48 0%,#35507a 45%,#16203a 100%)"></div>
    <h3 class="display">JETZT IST AGILITÄT GEFRAGT</h3>
    <p>Lorem ipsum dolor sit amet, consectetur adipiscing elit. Sodales adipiscing eget iaculis amet morbi. Egestas ipsum massa dolor gravida. A mattis viverra et malesuada mollis rhoncus tincidunt. Ante suspendisse sed risus est vitae convallis felis.</p>
    <a class="more">WEITERLESEN ›</a>
  </article>
</div>

<section class="newsletter" role="img" aria-label="Abgedunkeltes Foto eines Sportwagens als Hintergrund"></section>
<svg class="nl-icon" width="34" height="28" viewBox="0 0 34 28" fill="none" stroke="#e30613" stroke-width="1.6"><rect x="1" y="1" width="32" height="26" rx="2"/><path d="M1 3l16 12L33 3"/></svg>
<p class="nl-kicker">IMMER INFORMIERT</p>
<h2 class="nl-title">ZU UNSEREM NEWSLETTER</h2>
<form class="nl-form"><span class="nl-input">Deine E-Mail</span><span class="nl-submit">ABONNIEREN</span></form>

<div class="brand" style="left:131px;top:2790px;font-size:16px"><span>HALDRIS</span><span class="dot"></span></div>
<p class="copyright">© HALDRIS GMBH 2020</p>
<a class="footer-link" style="left:712px">KONTAKT</a>
<a class="footer-link" style="left:807px">AGB</a>
<a class="footer-link" style="left:873px">IMPRESSUM</a>
<a class="footer-link" style="left:981px">DATENSCHUTZ</a>

</body>
</html>
```